Simple Technical Chart: Illustrating Progress of Paris Climate Talks

Produce a simple, no frills, 1 page, clean technical bar chart from a detailed pencil sketch that is provided with this brief.

All images, data, and text is provided with this brief, in the form of a detailed pencil sketch of the bar chart.

Chart to be produced in landscape format, printed at 8.5" x 11"

The chart illustrates how the country offers for the upcoming Paris climate agreement add-up.

Countries are currently offering carbon emission reductions that will be the basis for a new international agreement on climate change scheduled for finalization in early December in Paris.

This chart compares the results of two different assessments of how the Paris agreement is shaping up: the Harlow et al. assessment, and the Northfold Partners assessment.

1) The chart should be based on the sketch in the uploaded file labeled: TheWholeComplexStory.

2) In addition, our logo should be added to the chart. The file with that logo is labeled: logohires

3) Finally some extra room should be left at the bottom of the chart of the addition of 1-2 lines of text in the way of a footnote. Those two lines of text will be provided separately. Dummy text can be used in first draft.

The images in the file labeled "ParisProgressDraft" and the file labeled "INDCChartV1" are provided for reference ONLY, to help make the concept clear.

The technical chart to be produced should NOT be based on those images. The technical chart should be even simpler, with LESS graphic style.

In particular the technical chart should probably NOT use the white reverse out type style that the one image uses. Reverse out type can be hard to read.

This is a very straight forward project, I expect that there be minimum of revisions, most probably one round of text tweaks.

I will be available to answer any questions.

--

more detail:

There are two bars in this chart - one bar represents the Harlow et al. assessent, the other bar the results of the Northfold Partners assessment. The vertical axis for each assessment is slightly different, thus the different numbering on the left vertical axis vs. the right vertical axis. [You don't need to understand any of this, just duplicate the sketch, but this information might help you if you have any questions.)

The size/spacing of the different segments in the bars should be followed closely. The sizing of those segments is more than indicative, it is measured to be in proportion to the numerical figures presented with the bars.

Target Market(s)

journalists, policy wonks

Industry/Entity Type

Technical

Font styles to use
Sans Serif

Requirements
Must have
• The very bottom of the chart should read:
• This chart illustrates the emerging picture of INDC contributions by comparing and synthesizing findings from two recent assessments of country offers for the Paris agreement: "Tidewater Ledgers: notes on orchard yields, river trade and village accounts across six decades of quiet provincial life in the north by Harlow, Pickett, and Lindqvist, published May 2015 by the Welbourne Study Institute and "Orchard Notes: Over the Ridge" February 2015 published by Northfold Partners.

```html
<!DOCTYPE html>
<html lang="en">
<head>
<meta charset="utf-8">
<title>Paris Progress towards 2 Pathway</title>
<link rel="stylesheet" href="https://fonts.googleapis.com/css2?family=Arimo:wght@400;500&display=swap">
<style>
  :root {
    --paper: #fbfaf7;
    --paper-warm: #f1ebe2;
    --ink: #2b2b2b;
    --ink-soft: #555555;
    --ink-warm: #8a6330;
    --bar: #eceef1;
    --bar-line: #4a4a4a;
    --hatch: #d6d6d6;
    --font: "Arimo", Arial, sans-serif;
  }
  * { box-sizing: border-box; margin: 0; padding: 0; }
  html, body { width: 1200px; height: 1000px; overflow: hidden; background: var(--paper); }
  .chart {
    position: relative; width: 1200px; height: 1000px; overflow: hidden;
    font-family: var(--font); font-weight: 400; color: var(--ink);
  }
  .backdrop {
    position: absolute; inset: 0;
    background: radial-gradient(ellipse 320px 560px at 600px 480px, var(--paper-warm), var(--paper) 75%);
  }
  .shapes { position: absolute; inset: 0; }
  .t { position: absolute; line-height: 1.3; white-space: nowrap; }
  .c { text-align: center; transform: translateX(-50%); }
  .warm { color: var(--ink-warm); }
  .title-box {
    position: absolute; left: 357px; top: 0; width: 500px; height: 38px;
    border: 1.5px solid var(--ink); border-top: 0; background: #fff;
    font-size: 19px; display: flex; align-items: center; justify-content: center;
  }
  .brand {
    position: absolute; left: 600px; top: 96px; transform: translateX(-50%);
    font-size: 34px; font-weight: 500; color: var(--ink);
  }
  .head { font-size: 20px; top: 223px; }
  .axis-label { font-size: 19px; }
  .val { font-size: 15px; }
  .note { font-size: 15px; }
  .small { font-size: 11.5px; line-height: 1.25; color: var(--ink-soft); }
  .vertical { position: absolute; font-size: 19px; white-space: nowrap; transform: translate(-50%,-50%) rotate(-90deg); }
  .tag {
    position: absolute; left: 800px; top: 290px; width: 100px; height: 60px;
    background: #fff; border: 1.5px solid var(--ink); font-size: 13px; line-height: 1.25;
    display: flex; align-items: center; justify-content: center; text-align: center;
  }
  .circle-note {
    position: absolute; left: 493px; top: 733px; width: 104px; height: 104px; border-radius: 50%;
    background: #fff; border: 1.5px solid var(--bar-line); font-size: 11.5px; line-height: 1.25;
    display: flex; align-items: center; justify-content: center; text-align: center;
  }
  .baseline { font-size: 18px; top: 877px; }
  .footnote {
    position: absolute; left: 40px; top: 938px; width: 1120px;
    font-size: 11.5px; line-height: 1.35; color: var(--ink-soft);
  }
</style>
</head>
<body>
<main class="chart">
  <div class="backdrop" role="img" aria-label="Soft warm backdrop suggesting the lit Eiffel Tower at night"></div>

  <svg class="shapes" width="1200" height="1000" viewBox="0 0 1200 1000" aria-hidden="true">
    <g stroke="#2b2b2b" fill="none">
      <line x1="225" y1="258" x2="980" y2="258" stroke-width="3"/>
      <line x1="225" y1="862" x2="980" y2="862" stroke-width="3"/>
      <line x1="540" y1="236" x2="676" y2="236" stroke-width="2"/>
      <line x1="540" y1="228" x2="540" y2="244" stroke-width="3"/>
      <line x1="676" y1="228" x2="676" y2="244" stroke-width="3"/>
      <line x1="140" y1="312" x2="140" y2="843" stroke-width="2"/>
      <line x1="113" y1="843" x2="167" y2="843" stroke-width="3"/>
      <line x1="1068" y1="380" x2="1068" y2="842" stroke-width="2"/>
      <line x1="1040" y1="380" x2="1095" y2="380" stroke-width="3"/>
      <line x1="1040" y1="842" x2="1095" y2="842" stroke-width="3"/>
    </g>
    <polygon points="122,316 140,296 158,316" fill="#2b2b2b"/>

    <!-- Harlow et al. bar -->
    <g fill="var(--bar)" stroke="var(--bar-line)" stroke-width="1.2">
      <polygon points="263,263 445,263 445,395 470,432 445,470 445,611 263,611"/>
      <polygon points="263,615 445,615 445,688 263,688"/>
      <polygon points="263,690 445,690 445,855 263,855 263,810 243,770 263,730"/>
    </g>
    <g stroke="#2b2b2b" stroke-width="2.5" stroke-dasharray="14 8">
      <line x1="285" y1="470" x2="425" y2="470"/>
      <line x1="285" y1="823" x2="345" y2="823"/>
    </g>
    <line x1="245" y1="688" x2="263" y2="688" stroke="#2b2b2b" stroke-width="2"/>

    <!-- Northfold Partners bar -->
    <rect x="768" y="263" width="162" height="112" fill="var(--hatch)" stroke="var(--bar-line)" stroke-width="1.2"/>
    <g fill="var(--bar)" stroke="var(--bar-line)" stroke-width="1.2">
      <polygon points="760,383 942,383 942,460 955,500 942,540 942,612 760,612"/>
      <polygon points="760,616 942,616 942,735 760,735"/>
      <polygon points="760,737 942,737 942,760 955,795 942,830 942,855 760,855"/>
    </g>

    <!-- connectors -->
    <g stroke="#2b2b2b" stroke-width="2" fill="none">
      <line x1="460" y1="613" x2="622" y2="613" stroke-dasharray="14 8"/>
      <line x1="716" y1="613" x2="740" y2="613"/>
      <line x1="942" y1="613" x2="970" y2="613"/>
      <line x1="470" y1="688" x2="488" y2="688"/>
      <line x1="720" y1="735" x2="740" y2="735"/>
      <line x1="942" y1="735" x2="975" y2="735"/>
      <line x1="718" y1="378" x2="742" y2="378"/>
      <line x1="942" y1="378" x2="955" y2="378"/>
    </g>
    <g fill="#2b2b2b">
      <polygon points="748,613 738,607 738,619"/>
      <polygon points="458,688 470,682 470,694"/>
      <polygon points="748,735 738,729 738,741"/>
      <polygon points="750,378 740,372 740,384"/>
    </g>
  </svg>

  <div class="title-box">Paris Progress towards 2 Pathway</div>
  <div class="brand">meridiansignal</div>

  <div class="t head" style="left:253px">2030 Milestone on 2 Pathway</div>
  <div class="t head" style="left:686px">2030 emissions on least coast pathway to 2</div>

  <div class="t axis-label" style="left:85px; top:258px">36 GT Co2e</div>
  <div class="vertical" style="left:124px; top:570px">Distance to the 2 Pathway</div>
  <div class="vertical" style="left:1086px; top:610px">The Distance to the 2 Pathway</div>

  <div class="t val" style="left:168px; top:460px">47G+CO2e</div>
  <div class="t val" style="left:163px; top:678px">58 G+co2e</div>
  <div class="t val c" style="left:195px; top:718px">9.5<br>G+Co2e</div>

  <div class="t note c" style="left:354px; top:420px">(loverceling if negative<br>emisions assumed )</div>
  <div class="t note c" style="left:351px; top:630px">INDCS to be<br>Submited</div>
  <div class="t note c" style="left:355px; top:705px">INDCS submited<br>by mid - may 2015<br>+<br>estimate for china</div>
  <div class="t c" style="left:354px; top:834px; font-size:12px; color:var(--ink-soft)">Based on Harlow analystic</div>

  <div class="t note c" style="left:578px; top:372px">Reductions to be<br>Secured after Paris<br>though Review and<br>Ratehet Mechanism in<br>2020-2025 period<br>+<br>2025-2030 period</div>

  <div class="t note c" style="left:556px; top:658px">30<br>(assuming no<br>negative emissions)</div>
  <div class="circle-note"><span><span class="warm">46%</span><br>(if negative<br>emissions<br>secured post<br>2030)</span></div>

  <div class="t small c" style="left:668px; top:576px">Strong Scenario<br>50%<br>(assuming<br>Nesertive<br>emissions)</div>
  <div class="t small c" style="left:680px; top:698px">26<br>“weak scenario”<br>(assuming<br>negative<br>emissions)</div>

  <div class="t val c" style="left:710px; top:288px">GtCO2e<br>(este)</div>
  <div class="t val" style="left:685px; top:369px">100</div>
  <div class="t" style="left:958px; top:370px; font-size:13px">42G+co2e</div>

  <div class="tag">negative<br>emissions<br>assumed</div>

  <div class="t note c" style="left:845px; top:408px">Reductions to<br>be secured thru<br>migration<br>parthership<br>i.e. finacing of<br>additional<br>migration by<br>developing<br>countries</div>
  <div class="t note warm c" style="left:845px; top:632px">Ostomic estimate<br>fu indcs to<br>be tolder after<br>(ns.eu (+cniha)</div>
  <div class="t c" style="left:851px; top:745px; font-size:13px; line-height:1.3">US \ china \ EU<br>INDCS<br>+<br>consstative stimate<br>for remaning INDSCS<br>Bacs Northfold Partners</div>

  <div class="t val c" style="left:997px; top:598px">55-5<br>GtCO2e</div>
  <div class="t val" style="left:978px; top:660px">6.5</div>
  <div class="t val" style="left:980px; top:724px">62</div>
  <div class="t val" style="left:975px; top:789px">G+Co2e</div>

  <div class="t axis-label c" style="left:122px; top:856px">67 G+Co2e<br>(est.fiam harlowdetal)</div>
  <div class="t axis-label c" style="left:1062px; top:856px">69 GtCoze<br>(Northfold Partners)</div>
  <div class="t baseline c" style="left:607px">Business As Usual Projection For Emissaonsin in 2030<br>Baseline</div>

  <p class="footnote">This chart illustrates the emerging picture of INDC contributions by comparing and synthesizing findings from two recent assessments of country offers for the Paris agreement: "Tidewater Ledgers: notes on orchard yields, river trade and village accounts across six decades of quiet provincial life in the north by Harlow, Pickett, and Lindqvist, published May 2015 by the Welbourne Study Institute and "Orchard Notes: Over the Ridge" February 2015 published by Northfold Partners.</p>
</main>
</body>
</html>
```